Modern Website Design for an Online Travel Agency.. Design Only!!

Hi there!

We are building an website for our travel agency that caters to tourists traveling to the Cayman Islands. We provide travel information and take bookings for various tours available here.

We need designs for 8 different web page layouts. You can see the layout specifications in two attached documents. We do not have a need for the coding to be done. This will simply act as a blueprint for our developer to build from.

The important pages are the 'Home Page' 'checkout page' and the ‘Checkout Page’ (Page 1 & 10 in the PDF ‘Website Layout’)

The MOST important page is ‘Tour Search Page’ (page 6)

If you intend on only submitting one page design, please submit a design for page 6. Be aware though, the more of these 3 page designs you submit, the more likely we are to move forward with you!

At this stage, we are simply looking to develop the most aesthetic website design layout possible.

- The website should be colour coordinated with the logo. You can most certainly use other colours if you feel they complement the overall design of the website well.

- Everything must be laid out in an EXTREMELY simple & ‘easy to navigate’ way. The key is simplicity & Functionality. There is no need for messy or elaborate graphics.

- The website MUST have a VERY clean and modern appearance.

- We want the main background to be white, but you can use light grey in places to compliment or add dimension if you feel necessary.

- We will appreciate a good use of shadows and especially a good use of icons. (You can see examples of icons we have already designed, we are definitely open to new icon design concepts too)

- We will reward imagination and original thinking! Essentially we want a website with a creative touch and unique design elements, whilst maintaining that clean and simple layout.

- Most importantly!! - Paying attention to the small details will be highly rewarded (A well balanced and seamless use of fonts, colours, dimensions, shadowing, positioning, etc)

If you have any questions, please don’t hesitate to ask.

We’re excited to see your design submissions!

Thank you!!

You can find all the support documents and content at: https://www.filevorra.net/sh/9qm2rtwplexan7c/QQBmTtZnPdLsWEGxvvaJpLmRw?dl=0

Target Market(s)

Tourists

Industry/Entity Type

Travel

Number of Pages Required

5+ page

Font styles to use
Sans Serif

Colors

Designer to choose colors to be used in the design.

Requirements
Must have
• Must be very clean and modern.
• Must be simple and bold
• Must be color coordinated in a way that makes sense
• White background
Nice to have
• Good use of shadows and Icons
Should not have
• Over use of messy graphics
• And design layout which is not right angled (using anything but vertical or horizontal for the edges in the design)

```html
<!DOCTYPE html>
<html lang="en">
<head>
<meta charset="utf-8">
<title>Checkout – TripIsle</title>
<link href="https://fonts.googleapis.com/css2?family=Montserrat:wght@400;500;600;700&family=Poppins:wght@600;700&display=swap" rel="stylesheet">
<style>
:root{
  --blue:#2f6db5;
  --blue-dark:#285f9f;
  --green:#8dc63f;
  --ink:#222;
  --muted:#8a8a8a;
  --footer:#25262b;
  --faq-bg:#f2f2f2;
  --red:#f00;
}
*{margin:0;padding:0;box-sizing:border-box}
html,body{width:676px;height:1200px;overflow:hidden;background:#fff}
body{position:relative;font-family:'Montserrat',sans-serif;color:var(--ink)}
.abs{position:absolute}

/* hero */
.hero{position:absolute;left:0;top:0;width:676px;height:199px;
  background:radial-gradient(ellipse at 50% 85%,#7a6a3a 0%,rgba(70,90,60,0) 45%),linear-gradient(180deg,#0c4a5a 0%,#16697a 45%,#1f7f86 70%,#385f4e 100%)}
.brand{left:53px;top:24px;display:flex;align-items:center;gap:4px;color:#fff;font-weight:700;font-size:14px;font-family:'Poppins',sans-serif}
.brand i{display:block;width:14px;height:14px;background:#fff}
.nav{left:213px;top:29px;display:flex;gap:12px;font-size:6.6px;color:#fff}
.nav .active{font-weight:700}
.dest{left:574px;top:7px;font-size:6.6px;color:#fff;font-weight:600}
.btn-outline{top:24px;height:18px;border:1px solid #fff;color:#fff;font-size:6.6px;font-weight:600;display:flex;align-items:center;justify-content:center;gap:3px}
.hero h1{position:absolute;left:0;width:676px;top:70px;text-align:center;color:#fff;font-family:'Poppins',sans-serif;font-weight:700;font-size:42px;letter-spacing:.5px}

/* tour cards */
.card{position:absolute;left:53px;width:424px;background:#fff;box-shadow:0 1px 5px rgba(0,0,0,.18)}
.card .photo{position:absolute;left:4px;top:4px;width:145px;height:169px}
.card h3{position:absolute;left:167px;top:25px;font-size:11px;font-weight:600}
.card .date{position:absolute;left:349px;top:24px;font-size:7.3px;display:flex;align-items:center;gap:4px;color:#444}
.card .meta{position:absolute;left:168px;font-size:7px;color:var(--muted)}
.card .meta b{color:var(--ink);font-weight:500}
.btn{position:absolute;height:21px;color:#fff;font-size:7px;font-weight:700;letter-spacing:1.3px;display:flex;align-items:center;justify-content:center}
.btn.green{background:var(--green)}
.btn.blue{background:var(--blue)}

/* booking service */
.service{position:absolute;left:53px;top:796px;width:424px;height:103px;background:#fff;box-shadow:0 1px 5px rgba(0,0,0,.18)}
.service h3{position:absolute;left:16px;top:18px;font-size:11px;font-weight:600;display:flex;align-items:center;gap:6px}
.free-badge{width:21px;height:21px;border-radius:50%;background:var(--red);color:#fff;font-size:5px;font-weight:700;display:flex;align-items:center;justify-content:center}
.service p{position:absolute;left:16px;top:46px;width:400px;font-size:7px;line-height:12.2px;color:#444}

/* sidebar */
.summary{position:absolute;left:492px;top:236px;width:131px;height:178px;background:var(--blue)}
.summary h2,.faq h2{height:28px;display:flex;align-items:center;justify-content:center;color:#fff;font-size:11.5px;font-weight:600;background:var(--blue-dark)}
.row{position:absolute;left:9px;width:109px;display:flex;justify-content:space-between;color:#fff;font-size:7px}
.sum-label{position:absolute;left:0;width:131px;text-align:center;color:#fff}
.faq{position:absolute;left:492px;top:427px;width:131px;height:170px;background:var(--faq-bg)}
.faq h2{background:var(--blue-dark)}
.faq ul{list-style:none;position:absolute;left:9px;top:43px;width:115px}
.faq li{font-size:6.2px;line-height:9.3px;color:#444;margin-bottom:4px;padding-left:8px;text-indent:-8px}
.faq li span{color:var(--blue);font-weight:700}

/* total */
.grand{left:0;width:530px;top:918px;text-align:center;font-size:20.5px;font-weight:500}
.grand span{color:var(--blue);font-weight:700}

/* footer */
.footer{position:absolute;left:0;top:1016px;width:676px;height:184px;background:var(--footer);color:#fff}
.f-brand{position:absolute;left:0;width:676px;top:20px;display:flex;justify-content:center;align-items:center;gap:6px;font-family:'Poppins',sans-serif;font-weight:700;font-size:23px;color:var(--green)}
.f-brand i{display:block;width:30px;height:30px;background:var(--green)}
.contact{position:absolute;top:82px;display:flex;align-items:center;gap:8px;font-size:10.5px;font-weight:400}
.divider{position:absolute;top:70px;width:1px;height:56px;background:#3a3b41}
.f-line{position:absolute;left:0;top:149px;width:676px;height:1px;background:#3a3b41}
.f-bottom{position:absolute;top:162px;font-size:6.5px;color:#ccc}
.f-bottom .hl{color:var(--green)}
</style>
</head>
<body>

<header class="hero">
  <div class="abs brand"><i></i>TripIsle</div>
  <nav class="abs nav">
    <span>Home</span><span>Discover Cayman</span><span>Thing to Do</span><span>My Trip Planner</span><span>Map</span><span class="active">Tours</span><span>Contact Us</span>
  </nav>
  <div class="abs dest">Destinations ⌄</div>
  <div class="abs btn-outline" style="left:526px;width:46px">USD$</div>
  <div class="abs btn-outline" style="left:577px;width:46px">
    <svg width="8" height="8" viewBox="0 0 10 10" fill="none" stroke="#fff" stroke-width="1"><path d="M4 1h5v8H4M1 5h5M4 3l2 2-2 2"/></svg>Login
  </div>
  <h1>Checkout Page</h1>
</header>

<!-- card 1 -->
<article class="card" style="top:236px;height:177px">
  <div class="photo" role="img" aria-label="Boy jumping into turquoise sea" style="background:linear-gradient(180deg,#6d9fd6 0%,#a9c8e8 40%,#3aa8b4 70%,#1f8e9a 100%)"></div>
  <h3>Pedro’s Castle</h3>
  <div class="date"><svg width="12" height="11" viewBox="0 0 12 11" fill="none" stroke="#2f6db5" stroke-width="1"><rect x=".5" y="1.5" width="11" height="9"/><path d="M.5 4h11M3 0v3M9 0v3M3 6h1M6 6h1M9 6h1M3 8h1M6 8h1M9 8h1"/></svg>17 Sept, 2019</div>
  <div class="meta" style="top:54px">Option: &nbsp;<b>Guided Tour</b></div>
  <div class="meta" style="top:73px">Adults : <b>2 Adults</b></div>
  <div class="meta" style="top:92px">Child: <b>1 Child</b></div>
  <div class="meta" style="top:111px">Cancellation Policy: &nbsp;<b>Flexible</b></div>
  <div class="btn green" style="left:166px;top:129px;width:57px">MODIFY</div>
  <div class="btn blue" style="left:228px;top:129px;width:57px">REMOVE</div>
</article>

<!-- card 2 -->
<article class="card" style="top:422px;height:177px">
  <div class="photo" role="img" aria-label="Person floating on an inflatable ring at sea" style="background:linear-gradient(180deg,#5b8fcf 0%,#c7d9ee 45%,#6a8fa4 60%,#2f5f72 100%)"></div>
  <h3>Flip Flop Tree</h3>
  <div class="date"><svg width="12" height="11" viewBox="0 0 12 11" fill="none" stroke="#2f6db5" stroke-width="1"><rect x=".5" y="1.5" width="11" height="9"/><path d="M.5 4h11M3 0v3M9 0v3M3 6h1M6 6h1M9 6h1M3 8h1M6 8h1M9 8h1"/></svg>18 Sept, 2019</div>
  <div class="meta" style="top:42px"><b>FREE</b></div>
  <div class="meta" style="top:54px">Cancellation Policy: &nbsp;<b>Flexible</b></div>
  <div class="btn green" style="left:166px;top:129px;width:57px">MODIFY</div>
  <div class="btn blue" style="left:228px;top:129px;width:57px">REMOVE</div>
</article>

<!-- card 3 -->
<article class="card" style="top:609px;height:177px">
  <div class="photo" role="img" aria-label="Stingrays swimming in clear shallow water" style="background:linear-gradient(160deg,#2aa6b8 0%,#4ec3c8 40%,#3a9aa0 70%,#1e6e80 100%)"></div>
  <h3>Pedro’s Castle</h3>
  <div class="date"><svg width="12" height="11" viewBox="0 0 12 11" fill="none" stroke="#2f6db5" stroke-width="1"><rect x=".5" y="1.5" width="11" height="9"/><path d="M.5 4h11M3 0v3M9 0v3M3 6h1M6 6h1M9 6h1M3 8h1M6 8h1M9 8h1"/></svg>17 Sept, 2019</div>
  <div class="meta" style="top:54px">Option: &nbsp;<b>Guided Tour</b></div>
  <div class="meta" style="top:73px">Adults : <b>2 Adults</b></div>
  <div class="meta" style="top:92px">Child: <b>1 Child</b></div>
  <div class="meta" style="top:111px">Cancellation Policy: &nbsp;<b>Flexible</b></div>
  <div class="btn green" style="left:166px;top:129px;width:57px">MODIFY</div>
  <div class="btn blue" style="left:228px;top:129px;width:57px">REMOVE</div>
</article>

<section class="service">
  <h3>Booking Service <span class="free-badge">FREE</span></h3>
  <p>Our local concierges take the time to double check your itinerary before booking. We may have recommendations based on local knowledge and will contact you if so. Once everything looks good, we make all the bookings on your behalf.</p>
</section>

<aside class="summary">
  <h2>Order Summery</h2>
  <div class="row" style="top:42px"><span>Pedros Castle</span><span>$45</span></div>
  <div class="row" style="top:58px"><span>Wakeboarding</span><span>$125</span></div>
  <div class="row" style="top:75px"><span>Horseriding</span><span>$350</span></div>
  <div class="row" style="top:91px"><span>Booking Service</span><span>FREE</span></div>
  <div class="sum-label" style="top:107px;font-size:11px">Total:</div>
  <div class="sum-label" style="top:120px;font-size:13px;font-weight:700">$520 USD</div>
  <div class="btn green" style="left:28px;top:144px;width:75px">CHECKOUT</div>
</aside>

<aside class="faq">
  <h2>FAQ’s</h2>
  <ul>
    <li><span>Q.</span> Duis eget consequat ex. Fusce mollis blandit dolor?</li>
    <li><span>Q.</span> Sed pellentesque risus cursus facilisis commodo?</li>
    <li><span>Q.</span> Sed pellentesque risus cursus facilisis commodo?</li>
    <li><span>Q.</span> Phasellus lobortis, ipsum ac effici tur ornare?</li>
    <li><span>Q.</span> Phasellus lobortis, ipsum ac effici tur ornare?</li>
  </ul>
</aside>

<div class="abs grand">Total: <span>$520 USD</span></div>
<div class="btn green" style="left:196px;top:958px;width:139px;height:24px;font-size:8px;letter-spacing:2px">CHECKOUT</div>

<footer class="footer">
  <div class="f-brand"><i></i>TripIsle</div>

  <div class="contact" style="left:89px">
    <svg width="28" height="28" viewBox="0 0 28 28" fill="none" stroke="#8dc63f" stroke-width="1"><rect x="5" y="5" width="18" height="18" rx="3" transform="rotate(45 14 14)"/><path d="M11 10l2 2-1 1c.5 1.5 1.5 2.5 3 3l1-1 2 2-1.5 1.5C13 18 10 15 9.5 11.5z"/></svg>
    <span>01-555-204-118</span>
  </div>
  <div class="divider" style="left:228px"></div>
  <div class="contact" style="left:271px">
    <svg width="28" height="28" viewBox="0 0 28 28" fill="none" stroke="#8dc63f" stroke-width="1"><rect x="5" y="5" width="18" height="18" rx="3" transform="rotate(45 14 14)"/><rect x="9" y="10.5" width="10" height="7"/><path d="M9 10.5l5 4 5-4"/></svg>
    <span>info@tripisle</span>
  </div>
  <div class="divider" style="left:434px"></div>
  <div class="contact" style="left:471px;align-items:flex-start">
    <svg width="28" height="28" viewBox="0 0 28 28" fill="none" stroke="#8dc63f" stroke-width="1"><rect x="5" y="5" width="18" height="18" rx="3" transform="rotate(45 14 14)"/><path d="M14 19s-4-4-4-7a4 4 0 018 0c0 3-4 7-4 7z"/><circle cx="14" cy="12" r="1.3"/></svg>
    <span style="line-height:13px;margin-top:2px">45 BC, making it<br>over 2000</span>
  </div>

  <div class="f-line"></div>
  <div class="f-bottom" style="left:53px">© 2019 <span class="hl">Trip Isle</span>. All Right Reserved.</div>
  <div class="f-bottom" style="left:499px">Privacy Policy &nbsp;&nbsp;| &nbsp;&nbsp;Term and Condition</div>
</footer>

</body>
</html>
```